Roof Plumbing Company needs simple, modern business card using the attached logo and below details:

Dean Halloway
Summit Gutters Pty Ltd
ABN: 58 214 937 062
Phone: 0417 286 531
Email: summitgutters@mailbrook.com
Website: summitgutters.com.au

For all of your metal roof plumbing requirements contact Summit Gutters for an obligation free quote - no job too big or to small!

Industry/Entity Type

Business

Contact Information for Business Card

Dean Halloway
Summit Gutters Pty Ltd
ABN 58 214 937 062
0417 286 531
summitgutters@mailbrook.com
summitgutters.com.au

Requirements
Must have
• Bright eye catching design, professional look

```html
<!DOCTYPE html>
<html lang="en">
<head>
<meta charset="utf-8">
<title>Summit Gutters Pty Ltd – Business Card</title>
<link rel="stylesheet" href="https://fonts.googleapis.com/css2?family=Open+Sans:wght@400;600;700&display=swap">
<style>
  :root {
    --page: #ececea;
    --charcoal: #2e2e2f;
    --white: #ffffff;
    --red: #d8262c;
    --red-dark: #b71c22;
    --grey: #555658;
    --grey-light: #9a9b9d;
    --ink: #4a4a4c;
  }
  * { box-sizing: border-box; margin: 0; padding: 0; }
  html, body {
    width: 1200px; height: 900px; overflow: hidden;
    background: var(--page);
    font-family: "Open Sans", Arial, sans-serif;
  }
  .sheet {
    position: relative; width: 1200px; height: 900px;
    display: flex; flex-direction: column; align-items: center;
    justify-content: center; gap: 40px;
  }
  .card {
    position: relative; width: 640px; height: 390px; overflow: hidden;
    box-shadow: 0 6px 18px rgba(0,0,0,0.18);
  }

  /* Back */
  .card--back {
    background: var(--charcoal); color: var(--white);
    display: flex; flex-direction: column; align-items: center; justify-content: center;
    gap: 36px; text-align: center; padding: 0 50px;
  }
  .brand-back {
    display: flex; align-items: center; gap: 14px;
    font-weight: 700; font-size: 34px; letter-spacing: 0.5px; color: var(--white);
  }
  .brand-back .mark { width: 22px; height: 22px; background: var(--white); }
  .tagline { font-size: 17px; line-height: 1.5; font-weight: 600; }

  /* Front */
  .card--front { background: var(--white); }
  .bands { position: absolute; inset: 0; }
  .name {
    position: absolute; left: 66px; top: 36px;
    font-size: 24px; font-weight: 700; color: var(--grey);
  }
  .name .first { color: var(--red); }
  .details { position: absolute; left: 40px; top: 140px; color: var(--ink); }
  .abn { font-size: 19px; font-weight: 700; color: var(--grey); margin-bottom: 14px; }
  .abn .label { color: var(--red); }
  .contact { list-style: none; font-size: 16px; line-height: 1.6; }
  .contact li { display: flex; align-items: center; gap: 10px; }
  .contact svg { width: 13px; height: 13px; flex: none; }
  .brand-front {
    position: absolute; right: 44px; top: 150px;
    display: flex; align-items: center; gap: 12px;
    font-weight: 700; font-size: 28px; color: var(--red-dark);
  }
  .brand-front .mark { width: 18px; height: 18px; background: var(--red-dark); }
</style>
</head>
<body>
<main class="sheet">
  <section class="card card--back" aria-label="Card back">
    <div class="brand-back"><span class="mark"></span>Summit Gutters Pty Ltd</div>
    <p class="tagline">For all of your metal roof plumbing requirements contact Summit Gutters<br>for an obligation free quote - no job too big or to small</p>
  </section>

  <section class="card card--front" aria-label="Card front">
    <svg class="bands" width="640" height="390" viewBox="0 0 640 390" aria-hidden="true">
      <defs>
        <linearGradient id="greyBand" x1="0" y1="0" x2="1" y2="0">
          <stop offset="0" stop-color="#6b6c6e"/>
          <stop offset="0.5" stop-color="#c9c9cb"/>
          <stop offset="1" stop-color="#e6e6e7"/>
        </linearGradient>
      </defs>
      <polygon points="0,0 58,0 40,28 0,28" fill="var(--red)"/>
      <polygon points="40,28 58,0 58,28" fill="var(--grey)"/>
      <polygon points="0,300 330,340 300,362 0,325" fill="var(--red)"/>
      <polygon points="300,362 330,340 640,378 640,390 300,390" fill="url(#greyBand)"/>
    </svg>

    <h1 class="name"><span class="first">Dean</span> Halloway</h1>

    <div class="details">
      <p class="abn"><span class="label">ABN</span> 58 214 937 062</p>
      <ul class="contact">
        <li><svg viewBox="0 0 16 16"><path fill="var(--red)" d="M3 1l3 3-2 2c1 2 3 4 6 6l2-2 3 3-2 2C7 15 1 9 1 3z"/></svg>0417 286 531</li>
        <li><svg viewBox="0 0 16 16"><rect x="1" y="3" width="14" height="10" fill="var(--red)"/><path d="M1 3l7 6 7-6" fill="none" stroke="#fff" stroke-width="1.5"/></svg>summitgutters@mailbrook.com</li>
        <li><svg viewBox="0 0 16 16"><g fill="none" stroke="var(--red)" stroke-width="2"><rect x="1" y="6" width="8" height="5" rx="2.5" transform="rotate(-45 5 8.5)"/><rect x="7" y="5" width="8" height="5" rx="2.5" transform="rotate(-45 11 7.5)"/></g></svg>www.summitgutters.com.au</li>
      </ul>
    </div>

    <div class="brand-front"><span class="mark"></span>Summit Gutters Pty Ltd</div>
  </section>
</main>
</body>
</html>
```